Flyer for Cool Choir Concert

8.5x11 color flyer, to get people to attend excellent concert

Requirements
Should not have
• I don't like a lot of musical symbols incorporated into the design.

```html
<!DOCTYPE html>
<html lang="en">
<head>
<meta charset="utf-8">
<title>War and Peace – Cantoria Southwest</title>
<link rel="stylesheet" href="https://fonts.googleapis.com/css2?family=Didact+Gothic&family=Kaushan+Script&family=Montserrat:ital,wght@0,500;0,600;1,400&display=swap">
<style>
  :root {
    --ink: #1c1414;
    --plum: #4a1a2e;
    --rust: #b4532f;
    --rule: #a9472a;
    --bg-light: #f6e6c4;
    --bg-mid: #e9caa6;
    --bg-edge: #c9a38f;
    --poppy: #e2543f;
    --poppy-deep: #b83426;
  }
  * { margin: 0; padding: 0; box-sizing: border-box; }
  html, body { width: 927px; height: 1200px; overflow: hidden; }
  body { font-family: "Didact Gothic", sans-serif; color: var(--ink); }

  .flyer { position: relative; width: 927px; height: 1200px; overflow: hidden; }

  .backdrop {
    position: absolute; inset: 0;
    background:
      radial-gradient(ellipse 200px 230px at 760px 870px, var(--poppy) 0%, rgba(226,84,63,.75) 45%, rgba(226,84,63,0) 100%),
      radial-gradient(ellipse 120px 120px at 640px 930px, rgba(184,52,38,.45), rgba(184,52,38,0) 100%),
      radial-gradient(ellipse 600px 420px at 620px 150px, #fbf0cf 0%, rgba(251,240,207,0) 100%),
      radial-gradient(ellipse 700px 700px at 460px 560px, var(--bg-light) 0%, var(--bg-mid) 65%, var(--bg-edge) 100%);
  }

  .content { position: relative; text-align: center; }

  .org-name {
    position: absolute; top: 62px; left: 0; right: 0;
    font-family: "Didact Gothic", sans-serif; font-size: 50px;
    letter-spacing: 3px; color: var(--plum); text-transform: uppercase;
  }
  .presents { position: absolute; top: 178px; left: 0; right: 0; font-size: 31px; letter-spacing: 1px; }
  .title {
    position: absolute; top: 222px; left: 0; right: 0;
    font-family: "Kaushan Script", cursive; font-size: 86px; font-weight: 400; line-height: 1;
  }
  .title .war { color: var(--plum); }
  .title .peace { color: var(--rust); }

  .intro {
    position: absolute; top: 352px; left: 160px; width: 607px;
    font-size: 19px; line-height: 25px;
  }
  .rule { position: absolute; left: 268px; width: 388px; height: 2px; background: var(--rule); }
  .rule.first { top: 487px; }
  .rule.second { top: 744px; }

  .dates {
    position: absolute; top: 512px; left: 0; right: 0;
    font-family: "Montserrat", sans-serif; font-weight: 600; font-size: 35px; line-height: 45px;
  }
  .venue {
    position: absolute; top: 606px; left: 0; right: 0;
    font-size: 27px; line-height: 44px; font-style: normal;
  }

  .tickets { position: absolute; top: 784px; left: 171px; width: 590px; text-align: left; }
  .tickets h2 { font-family: "Montserrat", sans-serif; font-weight: 500; font-size: 26px; line-height: 38px; }
  .price-row {
    display: flex; align-items: baseline;
    font-family: "Montserrat", sans-serif; font-weight: 600; font-size: 27px; line-height: 36px;
  }
  .price-row .leader { flex: 1; margin: 0 6px; border-bottom: 3px dotted var(--ink); transform: translateY(-6px); }
  .tickets .note { font-size: 16px; margin-top: 4px; }

  .staff {
    position: absolute; top: 1066px; left: 0; right: 0;
    font-family: "Montserrat", sans-serif; font-style: italic; font-size: 18px; line-height: 28px;
  }
  .website {
    position: absolute; top: 1118px; left: 0; right: 0;
    font-family: "Montserrat", sans-serif; font-weight: 600; font-size: 20px;
  }
</style>
</head>
<body>
<main class="flyer">
  <div class="backdrop" role="img" aria-label="Soft-focus photograph of a single red poppy on a warm golden background"></div>

  <div class="content">
    <div class="org-name">Cantoria Southwest</div>
    <p class="presents">PRESENTS</p>
    <h1 class="title"><span class="war">War</span> <span class="peace">and Peace</span></h1>

    <p class="intro">Join the singers of Cantoria Southwest as we perform music borne out of warfare and conflict, and music that celebrates peace and love. Featuring music of Aaron Whitcombe, Miriam Halvorsen, Owen Tarrant, Clara Penrose, and others.</p>

    <div class="rule first"></div>

    <p class="dates">Saturday, October 13 at 7:30pm<br>Sunday, October 14 at 3:00pm</p>

    <address class="venue">Grace Hill Community Church<br>1840 Mesa Verde Street<br>NE Albuquerque</address>

    <div class="rule second"></div>

    <section class="tickets">
      <h2>Tickets available online and at the door</h2>
      <div class="price-row"><span>General</span><span class="leader"></span><span>$20</span></div>
      <div class="price-row"><span>Seniors</span><span class="leader"></span><span>$15</span></div>
      <div class="price-row"><span>Students</span><span class="leader"></span><span>$10</span></div>
      <p class="note">Complimentary childcare provided at both performances.</p>
    </section>

    <p class="staff">Daniel Hartley, Artistic Director<br>Renata Olvera Sandoval, Executive Director</p>
    <p class="website">www.cantoria-abq.org</p>
  </div>
</main>
</body>
</html>
```